PowerPoint Design Project

Lanterfield Estate Partners is a Melbourne based property development management company. We provide a comprehensive range of development management services to a select group of listed developers, private landowners, overseas investors and development partners and institutional clients. Our website provides additional information about the company:
http://www.lanterfieldep.example.au
We are looking for a versatile powerpoint design that can be used across a wide variety of presentations including; pitch documents, client reports, Information memorandums, and downloadable credential packs etc. We have attached a good example document.
Updates

Industry/Entity Type

It Company

Requirements
Must have
• The design should have the following slides as a minimum: Intro Page, transition slides, profile slides, slides for graphics,

```html
<!DOCTYPE html>
<html lang="en">
<head>
<meta charset="utf-8">
<title>Lanterfield Estate Partners – Presentation Template</title>
<link href="https://fonts.googleapis.com/css2?family=Arimo:ital,wght@0,400;0,700&family=Italianno&display=swap" rel="stylesheet">
<style>
  :root {
    --canvas: #dfdfdf;
    --slide: #ffffff;
    --band-grey: #a9a9a9;
    --band-dark: #262626;
    --ink: #111111;
    --ink-soft: #333333;
    --accent-blue: #3fa3e6;
    --bullet-grey: #a5a5a5;
    --rule: #9a9a9a;
    --pie-red: #ff4a00;
    --pie-yellow: #ffb700;
    --pie-green: #7ba81a;
    --pie-blue: #46a6ee;
    --photo-fill: #c9c4b8;
  }
  * { box-sizing: border-box; margin: 0; padding: 0; }
  html, body { width: 1200px; height: 797px; overflow: hidden; }
  body {
    background: var(--canvas);
    font-family: "Arimo", Arial, sans-serif;
    color: var(--ink);
    position: relative;
  }
  h1, h2 { font-weight: 400; }
  .slide {
    position: absolute;
    width: 380px;
    height: 303px;
    background: var(--slide);
    overflow: hidden;
  }
  .slide--intro   { left: 18px;  top: 48px; }
  .slide--bullets { left: 412px; top: 48px; }
  .slide--profile { left: 805px; top: 48px; }
  .slide--process { left: 18px;  top: 401px; }
  .slide--chart   { left: 412px; top: 401px; }
  .slide--closing { left: 805px; top: 401px; }

  .header-band {
    position: absolute; left: 0; top: 0; width: 380px; height: 26px;
    background: var(--band-grey);
    clip-path: polygon(82px 0, 380px 0, 380px 26px, 108px 26px);
  }
  .slide-title {
    position: absolute; left: 112px; top: 6px;
    color: #fff; font-size: 14.5px; line-height: 16px; font-weight: 400;
  }
  .footer-band {
    position: absolute; left: 0; bottom: 0; width: 380px; height: 26px;
    background: var(--band-dark);
    clip-path: polygon(0 0, 310px 0, 337px 26px, 0 26px);
  }
  .footer-url {
    position: absolute; left: 8px; bottom: 7px;
    color: #fff; font-size: 9.5px; line-height: 11px;
  }
  .footer-name {
    position: absolute; left: 183px; bottom: 8px;
    color: #fff; font-size: 7.5px; font-weight: 700; letter-spacing: .2px;
    text-transform: uppercase; line-height: 9px; white-space: nowrap;
  }
  .page-number {
    position: absolute; right: 26px; bottom: 6px;
    color: var(--ink-soft); font-size: 13px; line-height: 14px;
  }
  .subtitle {
    position: absolute; left: 20px; top: 40px;
    color: var(--accent-blue); font-size: 9px;
  }
  .body-text { font-size: 9.2px; line-height: 11.4px; color: var(--ink); }

  /* Intro */
  .brand-name {
    position: absolute; left: 22px; top: 72px;
    font-size: 18px; font-weight: 700; color: var(--ink); text-transform: uppercase;
    white-space: nowrap; line-height: 22px;
  }
  .intro-title, .intro-subtitle {
    position: absolute; left: 0; width: 380px; text-align: center; font-size: 26px; font-weight: 400;
  }
  .intro-title { top: 173px; color: var(--accent-blue); }
  .intro-subtitle { top: 207px; color: var(--ink); }

  /* Bullets */
  .bullet-list { list-style: none; position: absolute; left: 34px; top: 61px; }
  .bullet-list li { position: absolute; left: 0; width: 320px; padding-left: 12px; }
  .bullet-list li::before {
    content: ""; position: absolute; left: 0; top: 2px;
    width: 7px; height: 7px; border-radius: 50%; background: var(--bullet-grey);
  }

  /* Profile */
  .profile-text { position: absolute; left: 22px; top: 58px; width: 210px; }
  .profile-text p + p { margin-top: 6px; }
  .profile-photo {
    position: absolute; left: 235px; top: 28px; width: 145px; height: 220px;
    background: var(--photo-fill);
  }

  /* Process */
  .process-intro { position: absolute; left: 22px; top: 60px; width: 340px; }
  .process-steps { position: absolute; left: 14px; top: 101px; width: 352px; height: 28px; }
  .process-step {
    position: absolute; top: 0; height: 28px; color: #fff; font-size: 9px;
    display: flex; align-items: center; justify-content: center;
  }
  .process-step--one { left: 0; width: 126px; background: var(--band-dark);
    clip-path: polygon(0 0, 114px 0, 126px 28px, 0 28px); }
  .process-step--two { left: 116px; width: 124px; background: var(--band-grey);
    clip-path: polygon(0 0, 110px 0, 124px 28px, 14px 28px); }
  .process-step--three { left: 226px; width: 126px; background: var(--band-dark);
    clip-path: polygon(0 0, 126px 0, 126px 28px, 14px 28px); }
  .process-detail { position: absolute; left: 13px; top: 148px; width: 355px; }

  /* Chart */
  .chart-intro { position: absolute; left: 22px; top: 60px; width: 340px; }
  .pie-chart { position: absolute; left: 71px; top: 74px; }
  .pie-label { font-family: "Arimo", Arial, sans-serif; font-size: 9px; fill: var(--ink); }
  .pie-label--light { fill: #fff; }

  /* Closing */
  .closing-message {
    position: absolute; left: 0; top: 88px; width: 380px; text-align: center;
    font-family: "Italianno", cursive; font-size: 38px; color: var(--accent-blue);
  }
  .closing-rule {
    position: absolute; left: 87px; top: 135px; width: 184px; height: 1px; background: var(--rule);
  }
</style>
</head>
<body>

<section class="slide slide--intro">
  <div class="header-band"></div>
  <div class="brand-name">Lanterfield Estate Partners</div>
  <h1 class="intro-title">Click to add Title</h1>
  <p class="intro-subtitle">Click to add subtitle</p>
  <div class="footer-band"></div>
  <span class="footer-url">www.lanterfieldep.example.au</span>
</section>

<section class="slide slide--bullets">
  <div class="header-band"></div>
  <h2 class="slide-title">Enter your title here</h2>
  <p class="subtitle">Enter your subtitle here</p>
  <ul class="bullet-list body-text">
    <li style="top:0">Lorem ipsum dolor sit amet<br>labore et dolore magna aliqua minim veniam.</li>
    <li style="top:34px">Lorem ipsum dolor sit amet<br>labore et dolore magna aliqua minim veniam.</li>
    <li style="top:67px">Lorem ipsum dolor sit amet<br>labore et dolore magna aliqua minim veniam.</li>
    <li style="top:135px">Lorem ipsum dolor sit amet<br>labore et dolore magna aliqua minim veniam.</li>
    <li style="top:166px">Lorem ipsum dolor sit amet<br>labore et dolore magna aliqua minim veniam.</li>
  </ul>
  <div class="footer-band"></div>
  <span class="footer-url">www.lanterfieldep.example.au</span>
  <span class="footer-name">Lanterfield Estate Partners</span>
  <span class="page-number">1</span>
</section>

<section class="slide slide--profile">
  <div class="header-band"></div>
  <h2 class="slide-title">Enter your title here</h2>
  <p class="subtitle">Enter your subtitle here</p>
  <div class="profile-text body-text">
    <p>Lorem ipsum dolor sit amet, consectetur adipisicing elit, sed do eiusmod tempor incididunt ut labore et dolore magna aliqua. Ut enim ad minim veniam, quis nostrud exercitation ullamco laboris nisi ut aliquip ex ea commodo</p>
    <p>dolor sit amet, consectetur adipisicing elit, sed do eiusmod tempor incididunt ut labore.</p>
    <p>dolor sit amet, consectetur adipisicing elit, sed do eiusmod tempor incididunt ut labore. Ut enim ad minim veniam, quis nostrud exercitation ullamco</p>
  </div>
  <div class="profile-photo" role="img" aria-label="Photo placeholder: project building with lawn"></div>
  <div class="footer-band"></div>
  <span class="footer-url">www.lanterfieldep.example.au</span>
  <span class="footer-name">Lanterfield Estate Partners</span>
  <span class="page-number">4</span>
</section>

<section class="slide slide--process">
  <div class="header-band"></div>
  <h2 class="slide-title">Enter your title here</h2>
  <p class="subtitle">Enter your subtitle here</p>
  <p class="process-intro body-text">dolor sit amet, consectetur adipisicing elit, sed do eiusmod tempor incididunt ut labore.</p>
  <div class="process-steps">
    <div class="process-step process-step--one">Lorem ipsum dolor sit</div>
    <div class="process-step process-step--two">Lorem ipsum dolor sit</div>
    <div class="process-step process-step--three">Lorem ipsum dolor sit</div>
  </div>
  <p class="process-detail body-text">dolor sit amet, consectetur adipisicing elit, sed do eiusmod tempor incididunt ut labore. Ut enim ad minim veniam, quis nostrud exercitation ullamco. dolor sit amet, consectetur adipisicing elit, sed do eiusmod tempor incididunt ut labore. Ut enim ad minim veniam, quis nostrud exercitation ullamco.</p>
  <div class="footer-band"></div>
  <span class="footer-url">www.lanterfieldep.example.au</span>
  <span class="footer-name">Lanterfield Estate Partners</span>
  <span class="page-number">7</span>
</section>

<section class="slide slide--chart">
  <div class="header-band"></div>
  <h2 class="slide-title">Enter your title here</h2>
  <p class="subtitle">Enter your subtitle here</p>
  <p class="chart-intro body-text">dolor sit amet, consectetur adipisicing elit, sed do eiusmod tempor incididunt ut labore.</p>
  <svg class="pie-chart" width="200" height="190" viewBox="0 0 200 190">
    <g transform="translate(100,95)">
      <path d="M-3,-3 L-3,-92 A92,92 0 0 0 -92,-3 Z" fill="var(--pie-red)"/>
      <path d="M3,-3 L92,-3 A92,92 0 0 0 3,-92 Z" fill="var(--pie-yellow)"/>
      <path d="M-3,3 L-92,3 A92,92 0 0 0 -3,92 Z" fill="var(--pie-green)"/>
      <path d="M3,3 L3,92 A92,92 0 0 0 92,3 Z" fill="var(--pie-blue)"/>
      <circle r="38" fill="#fff"/>
      <circle r="34" fill="var(--band-dark)"/>
      <text class="pie-label pie-label--light" x="0" y="3" text-anchor="middle">dolor sit amet</text>
      <text class="pie-label" x="-75" y="-46">dolor sit amet</text>
      <text class="pie-label" x="-75" y="-34">consectetur</text>
      <text class="pie-label" x="7" y="-46">sed do eiusmod</text>
      <text class="pie-label" x="-74" y="43">dolor sit amet</text>
      <text class="pie-label" x="17" y="43">dolor sitamet</text>
    </g>
  </svg>
  <div class="footer-band"></div>
  <span class="footer-url">www.lanterfieldep.example.au</span>
  <span class="footer-name">Lanterfield Estate Partners</span>
  <span class="page-number">12</span>
</section>

<section class="slide slide--closing">
  <div class="header-band"></div>
  <p class="closing-message">Thank you !</p>
  <div class="closing-rule"></div>
  <div class="footer-band"></div>
  <span class="footer-url">www.lanterfieldep.example.au</span>
  <span class="footer-name">Lanterfield Estate Partners</span>
  <span class="page-number">19</span>
</section>

</body>
</html>
```